Pro-life non-profit needs a dynamic poster design for their Christmas Gala.

We need a poster design which plays off the name of the event, The Winter Lantern. The Winter Lantern, of course is the Baby Jesus. Our cause supports unborn children in Iowa. The gala will include a concert of popular Christmas music sung by top soloists backed by an orchestra. An original commissioned song, The Winter Lantern, will be premiered. Purple and gold colors immediately come to mind, but a designer should not feel constrained on colors. We need an editable design w/fonts. Photoshop w/layers or Illustrator files are good.

```html
<!DOCTYPE html>
<html lang="en">
<head>
<meta charset="utf-8">
<title>The Winter Lantern – A Pro-Life Christmas Gala</title>
<link rel="stylesheet" href="https://fonts.googleapis.com/css2?family=Cinzel:wght@400;500;600&family=Great+Vibes&display=swap">
<style>
  :root {
    --page-bg: #d9d9db;
    --poster-dark: #1a1816;
    --straw-tone: #5a5246;
    --blanket-tone: #8a7c66;
    --text-light: #f2ece0;
    --gold-light: #fbe7a1;
    --gold-mid: #e0b440;
    --gold-deep: #b8862a;
  }
  * { margin: 0; padding: 0; box-sizing: border-box; }
  html, body {
    width: 1200px; height: 1200px; overflow: hidden;
    background: var(--page-bg);
  }
  .poster {
    position: absolute; left: 138px; top: 0;
    width: 924px; height: 1200px; overflow: hidden;
    background: var(--poster-dark);
    font-family: "Cinzel", serif;
    color: var(--text-light);
  }
  .poster-photo {
    position: absolute; inset: 0;
    background:
      radial-gradient(ellipse 70% 45% at 35% 88%, var(--blanket-tone) 0%, rgba(90,80,66,0.55) 45%, transparent 75%),
      radial-gradient(ellipse 80% 45% at 60% 18%, var(--straw-tone) 0%, rgba(60,54,46,0.5) 50%, transparent 80%),
      linear-gradient(180deg, #2a2622 0%, #1c1a18 45%, #2b2722 100%);
  }
  .gold {
    background: linear-gradient(180deg, var(--gold-light) 0%, var(--gold-mid) 50%, var(--gold-deep) 100%);
    -webkit-background-clip: text; background-clip: text;
    color: transparent;
  }
  .line {
    position: absolute; left: 0; width: 100%;
    text-align: center; line-height: 1; white-space: nowrap;
  }
  .presenter { top: 80px; font-size: 18px; }
  .banquet { top: 106px; font-size: 29px; }
  .title-the { top: 166px; font-size: 56px; font-weight: 500; }
  .title-main { top: 228px; font-size: 100px; font-weight: 500; letter-spacing: -2px; }
  .title-script {
    top: 300px; font-family: "Great Vibes", cursive;
    font-size: 150px; padding-left: 40px;
  }
  .subtitle { top: 480px; font-size: 39px; }
  .rule {
    position: absolute; height: 3px;
    background: linear-gradient(90deg, var(--gold-deep), var(--gold-light), var(--gold-mid));
  }
  .date-block { position: absolute; left: 128px; width: 247px; text-align: center; }
  .date-day { position: absolute; top: 548px; left: 128px; width: 247px; text-align: center; font-size: 90px; line-height: 1; }
  .date-day sup { font-size: 50px; vertical-align: -6px; }
  .date-weekday { top: 653px; font-size: 40px; line-height: 1; }
  .date-month { top: 699px; font-size: 26px; line-height: 1; }
  .info-block { position: absolute; left: 408px; width: 396px; text-align: center; line-height: 1; white-space: nowrap; }
  .doors { top: 568px; font-size: 29px; }
  .venue { top: 603px; font-size: 18px; }
  .price { top: 654px; font-size: 25px; }
  .extras { top: 687px; font-size: 16px; }
  .seating { top: 707px; font-size: 16px; }
  .speaker-label { top: 791px; font-size: 26px; }
  .speaker-name { top: 826px; font-size: 41px; }
  .contact-web { top: 900px; font-size: 18px; }
  .contact-phone { top: 923px; font-size: 18px; }
</style>
</head>
<body>
  <main class="poster">
    <div class="poster-photo" role="img" aria-label="Sepia photograph of a sleeping newborn resting on a woven blanket in a straw-filled manger"></div>

    <p class="line presenter">Prairie Hope Alliance presents</p>
    <p class="line banquet">The Tenth annual Fundraising Banquet</p>

    <h1>
      <span class="line title-the gold">THE</span>
      <span class="line title-main gold">WINTER</span>
      <span class="line title-script gold">Lantern</span>
    </h1>
    <p class="line subtitle">A Pro-Life Christmas Gala</p>

    <p class="date-day gold">21<sup>ST</sup></p>
    <div class="rule" style="left:128px; top:637px; width:247px;"></div>
    <p class="date-block date-weekday gold">SATURDAY</p>
    <p class="date-block date-month">November 2020</p>
    <div class="rule" style="left:128px; top:740px; width:247px;"></div>

    <p class="info-block doors">Doors open at 5:30 PM</p>
    <p class="info-block venue">Elm Ridge Hall, W. Des Moines, IA</p>
    <div class="rule" style="left:408px; top:637px; width:396px;"></div>
    <p class="info-block price">$60 person . $500 table of ten</p>
    <p class="info-block extras">Cocktails . Dinners . Christmas Concert</p>
    <p class="info-block seating">Seating Limited . Reservations Needed</p>
    <div class="rule" style="left:408px; top:740px; width:396px;"></div>

    <p class="line speaker-label">Special Guest Speaker</p>
    <p class="line speaker-name gold">Bishop Daniel Hartwell</p>

    <p class="line contact-web">ORDER TICKETS ONLINE: WWW.PRAIRIEHOPEALLIANCE.ORG</p>
    <p class="line contact-phone">515-555-0142 . EVENTS@PRAIRIEHOPEALLIANCE.ORG</p>
  </main>
</body>
</html>
```